The Seeds Of Quiet Harvest Inc.

On one side have the business name. On the other side have contact information. This is an indoor cannabis cultivation business. It’s a new company in Sacramento ca. So we need a logo designed. The company is Called the seeds of quiet harvest. We grow and distribute marijuana in California. We would like to see designers use the color green and communicate cultivation.

Target Market(s)

Networking

Contact Information for Business Card

Brent Tavaro: president
Phone: (916) 555-0147
Email: brent@theseedsofquietharvest.net

Logo Text

Not sure if i want text or just an image created by designers.

Font styles to use
Script

Colors
000000
9bcb3c
fbfcf7
cadf82

Requirements
Nice to have
• A classic elegant professional card.

```html
<!DOCTYPE html>
<html lang="en">
<head>
<meta charset="utf-8">
<title>The Seeds Of Quiet Harvest Inc. — Business Card</title>
<link rel="stylesheet" href="https://fonts.googleapis.com/css2?family=Open+Sans:wght@400;700;800&display=swap">
<style>
  :root {
    --backdrop: #3a3a37;
    --card: #0b0b0b;
    --green: #9bcb3c;
    --green-soft: #cadf82;
    --paper: #fbfcf7;
    --muted: #c9cac4;
  }
  * { box-sizing: border-box; margin: 0; padding: 0; }
  html, body {
    width: 1200px; height: 824px; overflow: hidden;
    background: var(--backdrop);
    font-family: "Open Sans", Arial, sans-serif;
  }
  .canvas {
    position: relative; width: 1200px; height: 824px;
    display: flex; align-items: center; justify-content: center; gap: 60px;
  }
  .card {
    width: 520px; height: 298px;
    background: var(--card);
    border-radius: 4px;
    box-shadow: 0 10px 30px rgba(0,0,0,.45);
    position: relative;
    overflow: hidden;
  }
  .wordmark {
    color: var(--green);
    font-weight: 800;
    line-height: 1.05;
    display: flex; align-items: center; gap: 10px;
    white-space: nowrap;
  }
  .wordmark-dot {
    flex: none; border-radius: 50%; background: var(--green);
  }
  /* front */
  .card-front { display: flex; align-items: center; justify-content: center; }
  .card-front .wordmark { font-size: 38px; gap: 12px; }
  .card-front .wordmark-dot { width: 26px; height: 26px; }
  /* back */
  .card-back .wordmark {
    position: absolute; left: 34px; top: 98px; font-size: 22px;
  }
  .card-back .wordmark-dot { width: 15px; height: 15px; }
  .contact {
    position: absolute; left: 262px; right: 24px; top: 122px;
  }
  .contact-name {
    color: var(--paper); font-weight: 800; font-size: 19px; letter-spacing: .2px;
  }
  .contact-role {
    color: var(--green); font-weight: 700; font-size: 11.5px; margin-top: 1px;
  }
  .contact-list { list-style: none; margin-top: 12px; }
  .contact-item {
    display: flex; align-items: center; gap: 9px;
    color: var(--muted); font-size: 11.5px; margin-bottom: 8px;
    white-space: nowrap;
  }
  .contact-icon { width: 11px; height: 11px; flex: none; }
</style>
</head>
<body>
<main class="canvas">
  <section class="card card-front" aria-label="Card front">
    <div class="wordmark">
      <span class="wordmark-dot"></span>
      <span class="wordmark-text">The Seeds Of<br>Quiet Harvest</span>
    </div>
  </section>

  <section class="card card-back" aria-label="Card back">
    <div class="wordmark">
      <span class="wordmark-dot"></span>
      <span class="wordmark-text">The Seeds Of<br>Quiet Harvest</span>
    </div>
    <div class="contact">
      <p class="contact-name">Brent Tavaro</p>
      <p class="contact-role">President</p>
      <ul class="contact-list">
        <li class="contact-item">
          <svg class="contact-icon" viewBox="0 0 12 12" aria-hidden="true">
            <path d="M1 4.5 Q6 1 11 4.5 L10 6 L8 5 L8 4 Q6 3.3 4 4 L4 5 L2 6 Z" fill="#9bcb3c"/>
            <rect x="2.5" y="6.5" width="7" height="4.5" rx="1" fill="#9bcb3c"/>
          </svg>
          <span>(916) 555-0147</span>
        </li>
        <li class="contact-item">
          <svg class="contact-icon" viewBox="0 0 12 12" aria-hidden="true">
            <rect x="0.5" y="2.5" width="11" height="7.5" rx="1" fill="#9bcb3c"/>
            <path d="M1 3 L6 7 L11 3" fill="none" stroke="#0b0b0b" stroke-width="1"/>
          </svg>
          <span>brent@theseedsofquietharvest.net</span>
        </li>
      </ul>
    </div>
  </section>
</main>
</body>
</html>
```